redesign of www.varqolo.com

Need redesign of our website to be more professionally looking. International import & export, warehousing and distribution business primarily from China to North America.

A few professional pictures needed on the new website.

Contact form also is needed.

Total 5 - 10 pages will be OK.

```html
<!DOCTYPE html>
<html lang="en">
<head>
<meta charset="utf-8">
<title>Varqolo – Global Trade and Logistics Partner</title>
<link rel="stylesheet" href="https://fonts.googleapis.com/css2?family=Arimo:wght@400;700&family=Ropa+Sans&display=swap">
<style>
:root{
  --orange:#f39a0c;
  --orange-light:#fbb53a;
  --ink:#1e1e1e;
  --muted:#444;
  --bar-light:#ececec;
  --footer:#4b4b4b;
  --link-red:#b2320f;
  --page:#ffffff;
}
*{margin:0;padding:0;box-sizing:border-box}
html,body{width:957px;height:1200px;overflow:hidden;background:var(--page)}
body{position:relative;font-family:"Arimo",Arial,sans-serif;color:var(--ink)}
.abs{position:absolute}
h1,h2{font-weight:400}

/* header */
.brand{left:82px;top:24px;display:flex;align-items:center;gap:12px}
.brand-mark{width:16px;height:16px;border-radius:50%;background:var(--orange)}
.brand-name{font-family:"Ropa Sans",sans-serif;font-size:34px;color:var(--orange);line-height:1}
.brand-divider{left:207px;top:24px;width:1px;height:54px;background:#555;transform:rotate(8deg)}
.brand-tagline{left:221px;top:36px;font-size:7.5px;font-style:italic;line-height:9px;color:#333}
.call{left:774px;top:34px;display:flex;gap:12px;align-items:center}
.call-text{font-size:9.5px;line-height:17px;color:#222}

/* nav */
.nav{left:80px;top:92px;width:798px;height:46px;display:flex;background:linear-gradient(#555,#333);border-bottom:4px solid var(--orange)}
.nav-home{width:105px;background:linear-gradient(var(--orange-light),var(--orange));display:flex;align-items:center;justify-content:center}
.nav-item{color:#fff;font-size:11.5px;display:flex;align-items:center;justify-content:center;border-left:1px solid #222;box-shadow:inset 1px 0 #666}
.nav-item.about{width:134px}.nav-item.services{width:121px}.nav-item.products{width:122px}.nav-item.news{width:164px}.nav-item.contact{flex:1}

/* hero */
.hero{left:80px;top:138px;width:798px;height:323px;background:linear-gradient(120deg,#6d5a4f 0%,#b7a89a 35%,#d9d6cf 60%,#8e8272 85%,#5e5048 100%)}
.hero-caption{left:98px;top:203px;width:381px;height:186px;background:rgba(80,80,80,.72);padding:16px 18px}
.hero-title{font-family:"Ropa Sans",sans-serif;font-size:22px;color:#fff}
.hero-text{margin-top:14px;font-size:9.2px;line-height:17.6px;color:#f2f2f2}
.hero-dots{display:flex;gap:5px;margin-top:26px}
.dot{width:11px;height:11px;border-radius:50%;background:#fff;border:3px solid #dcdcdc;box-shadow:0 0 0 1px #888}
.dot.active{background:var(--orange)}

/* welcome */
.welcome-photo{left:81px;top:500px;width:187px;height:160px;background:linear-gradient(90deg,#a98258,#e8e6e2 45%,#e8e6e2 55%,#a98258)}
.welcome-title{left:286px;top:500px;font-family:"Ropa Sans",sans-serif;font-size:14px;color:#222}
.welcome-text{left:286px;top:526px;width:310px;font-size:9.2px;line-height:19.2px;color:var(--muted);white-space:nowrap}
.learn-more{left:500px;top:648px;width:89px;text-align:right;font-size:9.5px;color:var(--link-red);text-decoration:none}
.gallery{left:629px;top:497px;width:252px;height:166px;border:3px solid #1a1a1a;border-radius:3px;background:linear-gradient(180deg,#dfe3e6 0%,#cfc9bf 45%,#a98f6c 70%,#5b86b8 100%)}
.gallery-next{left:109px;top:53px;width:50px;height:50px;border-radius:50%;background:rgba(50,50,50,.75);display:flex;align-items:center;justify-content:center}

/* service columns */
.col{top:702px;width:235px}
.col.one{left:80px}.col.two{left:361px}.col.three{left:644px}
.col-head{height:42px;background:linear-gradient(var(--orange-light),var(--orange));color:#fff;font-family:"Ropa Sans",sans-serif;font-size:14.5px;display:flex;align-items:center;justify-content:center;box-shadow:0 3px 3px -2px #ccc}
.col-photo{margin-top:14px;height:150px;box-shadow:0 3px 3px -2px #bbb}
.col.one .col-photo{background:linear-gradient(180deg,#b7a590 0%,#c8c2b8 40%,#d6d3cf 55%,#b43a3a 70%,#6e6e6e 100%)}
.col.two .col-photo{background:linear-gradient(160deg,#9fb9d6 0%,#c9d6e2 40%,#6e6a64 65%,#2e2c2a 100%)}
.col.three .col-photo{background:linear-gradient(135deg,#7da6d6 0%,#2f6aa8 45%,#15365f 100%)}
.col-text{margin-top:16px;margin-left:-6px;margin-right:-6px;font-size:9.2px;line-height:17.6px;color:#222;text-align:center;white-space:nowrap}

/* contact bar */
.contact-bar{left:80px;top:1050px;width:798px;height:60px;background:var(--bar-light);font-size:10.8px;color:#111}
.contact-item{position:absolute;top:20px;display:flex;align-items:center;gap:10px}

/* footer */
.footer{left:80px;top:1110px;width:798px;height:65px;background:var(--footer);color:#fff;font-size:9.5px}
.footer-links{position:absolute;left:18px;top:27px}
.social{position:absolute;left:385px;top:18px;display:flex;gap:12px}
.social span{width:25px;height:25px;border-radius:50%;background:linear-gradient(#f2f2f2,#bdbdbd)}
.copyright{position:absolute;right:14px;top:27px}
</style>
</head>
<body>

<header>
  <div class="abs brand"><span class="brand-mark"></span><span class="brand-name">Varqolo</span></div>
  <div class="abs brand-divider"></div>
  <div class="abs brand-tagline">Global Trade<br>and Logistics<br>Partner</div>
  <div class="abs call">
    <svg width="14" height="22" viewBox="0 0 14 22"><rect x="1" y="1" width="12" height="20" rx="2" fill="none" stroke="#222" stroke-width="2"/><rect x="3" y="4" width="8" height="12" fill="#222"/><circle cx="7" cy="18.3" r="1" fill="#222"/></svg>
    <div class="call-text">GIVE US A CALL:<br>+1 800 555 0147</div>
  </div>
</header>

<nav class="abs nav">
  <div class="nav-home">
    <svg width="22" height="20" viewBox="0 0 22 20"><path d="M11 1 L21 10 H18 V19 H13 V13 H9 V19 H4 V10 H1 Z" fill="#fff"/></svg>
  </div>
  <div class="nav-item about">About Us</div>
  <div class="nav-item services">Services</div>
  <div class="nav-item products">Products</div>
  <div class="nav-item news">News and Events</div>
  <div class="nav-item contact">Contact Us</div>
</nav>

<section class="abs hero" role="img" aria-label="Warehouse aisle with stocked shelving and a moving forklift"></section>
<div class="abs hero-caption">
  <h1 class="hero-title">International import &amp; export</h1>
  <p class="hero-text">Donec pharetra, lectus nec dignissim pharetra, leo felis dapibus nunc, eu laoreet lorem nibh quis libero. Nulla facilisi. Sed pulvinar sem nec tortor.Donec pharetra, lectus nec dignissim pharetra, leo felis dapibus nunc, eu laoreet lorem nibh quis libero. Nulla facilisi. Sed pulvinar sem nec tortor.</p>
  <div class="hero-dots"><span class="dot active"></span><span class="dot"></span><span class="dot"></span><span class="dot"></span></div>
</div>

<section>
  <div class="abs welcome-photo" role="img" aria-label="Worker walking down a warehouse aisle lined with boxes"></div>
  <h2 class="abs welcome-title">Welcome To Varqolo</h2>
  <p class="abs welcome-text">Lorem ipsum dolor sit amet conse ctetur adipisicing elit, sed do eiusmod<br>tempor incididunt ut labore et dolore magna aliqua. Ut enim ad minim<br>veniam, quis nostrud exercitation ullamco laboris.Lorem ipsum dolor sit<br>amet conse ctetur adipisicing elit, sed do eiusmod tempor incididunt ut<br>labore et dolore magna aliqua. Ut enim ad minim veniam,&nbsp; magna aliqua.<br>Ut enim ad minim veniam,</p>
  <a class="abs learn-more" href="#">Learn More</a>
  <div class="abs gallery" role="img" aria-label="Storage room with cardboard drums on blue pallets">
    <div class="abs gallery-next"><svg width="12" height="20" viewBox="0 0 12 20"><path d="M2 2 L10 10 L2 18" fill="none" stroke="#fff" stroke-width="3"/></svg></div>
  </div>
</section>

<section>
  <div class="abs col one">
    <div class="col-head">International import &amp; export</div>
    <div class="col-photo" role="img" aria-label="Row of red and white trucks parked by brick buildings"></div>
    <p class="col-text">Lorem ipsum dolor sit amet, consectetur adipisicing<br>elit, sed do eiusmod tempor et dolore magna<br>aliqua.Lorem ipsum dolor sit amet, consectetur Lorem<br>ipsum dolor sit amet, consectetur adipisicing elit, sed<br>do eiusmod tempor et dolore magna aliqua.</p>
  </div>
  <div class="abs col two">
    <div class="col-head">Distribution &amp; Warehousing</div>
    <div class="col-photo" role="img" aria-label="Silver truck with a white trailer on the road"></div>
    <p class="col-text">Lorem ipsum dolor sit amet, consectetur adipisicing<br>elit, sed do eiusmod tempor et dolore magna<br>aliqua.Lorem ipsum dolor sit amet, consectetur Lorem<br>ipsum dolor sit amet, consectetur adipisicing elit, sed<br>do eiusmod tempor et dolore magna aliqua.</p>
  </div>
  <div class="abs col three">
    <div class="col-head">Varqolo's Principle</div>
    <div class="col-photo" role="img" aria-label="Blue-toned collage of an airplane, world map and shipping containers"></div>
    <p class="col-text">Lorem ipsum dolor sit amet, consectetur adipisicing<br>elit, sed do eiusmod tempor et dolore magna<br>aliqua.Lorem ipsum dolor sit amet, consectetur Lorem<br>ipsum dolor sit amet, consectetur adipisicing elit, sed<br>do eiusmod tempor et dolore magna aliqua.</p>
  </div>
</section>

<footer>
  <div class="abs contact-bar">
    <div class="contact-item" style="left:24px">
      <svg width="14" height="22" viewBox="0 0 14 22"><path d="M7 1 C3 1 1 4 1 7 C1 12 7 21 7 21 C7 21 13 12 13 7 C13 4 11 1 7 1 Z" fill="#111"/><circle cx="7" cy="7" r="2.3" fill="#ececec"/></svg>
      <span>2150 Harbourline Rd, Suite 300, Eastvale, ON, L4K 2T9, Canada</span>
    </div>
    <div class="contact-item" style="left:410px">
      <svg width="20" height="20" viewBox="0 0 20 20"><path d="M4 1 L8 5 L6 8 C7 11 9 13 12 14 L15 12 L19 16 L16 19 C8 18 2 12 1 4 Z" fill="#111"/></svg>
      <span>Tel : 416 555 0182, Fax : 416 555 0196</span>
    </div>
    <div class="contact-item" style="left:659px">
      <svg width="26" height="18" viewBox="0 0 26 18"><rect x="0" y="0" width="26" height="18" rx="2" fill="#111"/><path d="M1 2 L13 11 L25 2" fill="none" stroke="#ececec" stroke-width="2"/></svg>
      <span>info@varqolo.com</span>
    </div>
  </div>
  <div class="abs footer">
    <div class="footer-links">Home &nbsp;| &nbsp;Services &nbsp;|, About | International import &amp; export | &nbsp;Contact us</div>
    <div class="social"><span></span><span></span><span></span><span></span><span></span></div>
    <div class="copyright">© 2014 Varqolo Inc. All Rights Reserved.</div>
  </div>
</footer>

</body>
</html>
```